Web Design - Fitness for Middle Age Women

I need a web design for a start-up personal training company in Los Alamitos, CA called 'Maple Fitness & Health.' I would like to cater personal training services to middle-age mothers (30-50 years of age) who have kids and who would also want their children to receive services. The attached file is the logo of the company. Keep in mind the theme colors are white and blue and black, but make the background/pictures appealing to middle-age mothers. I want the flow of the website to be easy to use. The final design should present the company as a professional personal training service.

I realize this is a low budget project for designers but this is a budget I have to offer at the moment and if I take your design I will make sure to come back to improve the site when I'm able to gain more capital. I am looking for a full website built (using wordpress) with the following tabs (About / FAQ / Services / Clients / Location / Contact Us...and social media links to Twitter / Instagram / Facebook)
Updates

I am looking over the current designs and narrowing down the decision. A decision will be made in the next 24-48 hours.

Target Market(s)

Middle-age mothers (30-55 years of age) who have children, an established career (or husband who is the bread-winner of the house) and has forgotten to take care of themselves and their body for years. I want them to realize lifestyle change is a choice, and it is a choice they need to make for themselves and their family to be a proper pattern for their children.

Industry/Entity Type

Fitness

Requirements
Must have
• The logo I have attached.

```html
<!DOCTYPE html>
<html lang="en">
<head>
<meta charset="utf-8">
<title>Maple Fitness &amp; Health</title>
<link rel="stylesheet" href="https://fonts.googleapis.com/css2?family=Open+Sans:wght@400;600;700&family=Oswald:wght@400;500&display=swap">
<style>
:root{
  --navy:#14104f;
  --ink:#222222;
  --text:#666666;
  --muted:#8a8a8a;
  --band:#e6e6e6;
  --rule:#e2e2e2;
  --page:#ffffff;
  --stage:#f2f2f2;
  --hero-dark:#000000;
}
*{box-sizing:border-box;margin:0;padding:0}
html,body{width:1200px;height:1000px;overflow:hidden}
body{background:var(--stage);font-family:"Open Sans",Arial,sans-serif;color:var(--ink);position:relative}
.page{position:absolute;left:199px;top:0;width:802px;height:1000px;background:var(--page);box-shadow:0 0 60px rgba(0,0,0,.12)}
.abs{position:absolute}
/* header */
.brand{left:186px;top:12px;display:flex;align-items:center;gap:6px}
.brand-mark{width:32px;height:32px;border-radius:50%;background:var(--navy)}
.brand-name{font-size:9px;line-height:11px;color:var(--navy);font-weight:400;letter-spacing:.3px;white-space:nowrap}
.nav{left:0;top:0;width:802px;height:57px}
.nav a{position:absolute;top:0;display:flex;align-items:center;justify-content:center;font-size:9px;color:var(--ink);text-decoration:none;text-transform:uppercase;height:57px;white-space:nowrap;padding-top:3px}
.nav .current{left:353px;width:53px;background:var(--navy);color:#fff}
.nav .about{left:445px}
.nav .contact{left:527px}
/* hero */
.hero{left:0;top:57px;width:802px;height:211px;background:var(--hero-dark)}
.hero-photo{position:absolute;left:156px;top:0;width:488px;height:211px;background:linear-gradient(180deg,#cfc9b9 0%,#b7ab97 45%,#6f6558 100%)}
/* features */
.features{left:0;top:268px;width:802px;height:115px;background:var(--band)}
.feature{position:absolute;top:33px;width:160px}
.feature .ico{position:absolute;left:0;top:0;width:30px;height:30px;border-radius:50%;background:var(--navy);display:flex;align-items:center;justify-content:center}
.feature h3{position:absolute;left:42px;top:0;font-size:9px;font-weight:400;text-transform:uppercase;letter-spacing:.3px;color:var(--ink)}
.feature p{position:absolute;left:42px;top:18px;width:118px;font-size:5.4px;line-height:10.5px;color:var(--muted)}
.more-link{color:var(--navy);font-weight:700}
/* intro */
.intro-title{left:156px;top:416px;width:325px;font-size:8.6px;font-weight:700;line-height:11px;text-transform:uppercase;color:var(--ink)}
.rule{height:1px;background:var(--rule)}
.intro-sub{left:156px;top:450px;font-size:8px;color:var(--navy)}
.col{position:absolute;top:474px;width:152px}
.col h4{font-size:6px;font-weight:700;color:var(--ink);margin-bottom:3px}
.col p{font-size:5.4px;line-height:10.4px;color:var(--muted)}
.pill{position:absolute;background:var(--navy);color:#fff;border-radius:8px;font-family:"Oswald",sans-serif;font-size:5.5px;display:flex;align-items:center;justify-content:center;letter-spacing:.3px}
.intro-photo{left:497px;top:417px;width:148px;height:148px;border-radius:50%;background:radial-gradient(circle at 50% 40%,#e9eef0 0%,#9fb18a 55%,#56683e 100%)}
/* banner */
.banner{left:156px;top:599px;width:489px;height:77px;background:var(--navy);border-radius:4px;color:#fff}
.banner .avatar{position:absolute;left:12px;top:20px;width:30px;height:30px;border-radius:50%;background:#fff;display:flex;align-items:center;justify-content:center}
.banner h5{position:absolute;top:18px;font-family:"Oswald",sans-serif;font-weight:400;font-size:8.4px;letter-spacing:.4px;text-transform:uppercase}
.banner .quote{position:absolute;left:53px;top:35px;width:190px;font-size:6px;line-height:10.5px}
.banner .quote em{font-size:5px;font-weight:600}
.field{position:absolute;background:#fff;border-radius:9px;color:#aaa;font-size:4.8px;font-style:italic;padding-left:7px;display:flex;align-items:center}
.subscribe{position:absolute;left:427px;top:40px;width:49px;height:17px;border-radius:9px;background:#fff;color:var(--navy);font-family:"Oswald",sans-serif;font-size:5.5px;display:flex;align-items:center;justify-content:center}
/* lower */
.lower-title{position:absolute;top:705px;font-size:8.5px;font-weight:400;text-transform:uppercase;letter-spacing:.3px;color:var(--ink)}
.post-thumb{position:absolute;left:156px;width:29px;height:29px;border-radius:50%}
.post-text{position:absolute;left:198px;width:118px;font-size:5.4px;line-height:10px;color:var(--muted)}
.post-text b{color:var(--navy);font-weight:600}
.form-box{left:323px;top:725px;width:155px;height:163px;background:var(--band)}
.form-box p{position:absolute;left:13px;top:12px;width:130px;font-size:5.3px;line-height:10px;color:var(--muted)}
.contact-item{position:absolute;left:491px;width:155px}
.contact-item svg{position:absolute;left:0;top:0}
.contact-item h6{position:absolute;left:20px;top:0;font-size:6px;font-weight:700;color:var(--navy)}
.contact-item p{position:absolute;left:20px;top:10px;font-size:5.2px;line-height:10px;color:var(--muted)}
/* footer */
.footer{left:0;top:914px;width:802px;height:86px;background:var(--navy)}
.social{position:absolute;top:33px;width:18px;height:18px;border-radius:50%;background:#fff}
</style>
</head>
<body>
<div class="page">
  <header>
    <div class="abs brand"><span class="brand-mark"></span><span class="brand-name">MAPLE<br>Fitness &amp; Health</span></div>
    <nav class="abs nav"><a class="current" href="#">Home</a><a class="about" href="#">About us</a><a class="contact" href="#">Contact</a></nav>
  </header>

  <section class="abs hero"><div class="hero-photo" role="img" aria-label="Group of women doing a yoga pose in a bright studio"></div></section>

  <section class="abs features">
    <div class="feature" style="left:156px">
      <div class="ico"><svg width="16" height="10" viewBox="0 0 16 10"><rect x="0" y="3" width="2" height="4" fill="#fff"/><rect x="2.5" y="1" width="2.5" height="8" fill="#fff"/><rect x="5" y="4" width="6" height="2" fill="#fff"/><rect x="11" y="1" width="2.5" height="8" fill="#fff"/><rect x="14" y="3" width="2" height="4" fill="#fff"/></svg></div>
      <h3>Facility</h3>
      <p>Donec nec justo eget felis facilisis fermentum. Aliquam porttitor mauris sit amet orci. Aenean dignissim pellentesq <span class="more-link">=&gt; more</span></p>
    </div>
    <div class="feature" style="left:323px">
      <div class="ico"><svg width="14" height="13" viewBox="0 0 14 13"><path d="M7 12 1.2 6.3A3.3 3.3 0 0 1 7 2.3a3.3 3.3 0 0 1 5.8 4Z" fill="#fff"/><path d="M2 6.5h3l1-2 1.5 4 1-2H12" stroke="var(--navy)" stroke-width="1" fill="none"/></svg></div>
      <h3>Health</h3>
      <p>Donec nec justo eget felis facilisis fermentum. Aliquam porttitor mauris sit amet orci. Aenean dignissim pellentesq <span class="more-link">=&gt; more</span></p>
    </div>
    <div class="feature" style="left:491px">
      <div class="ico"><svg width="16" height="16" viewBox="0 0 16 16"><circle cx="8" cy="3" r="2" fill="#fff"/><rect x="6" y="5.5" width="4" height="6" rx="1" fill="#fff"/><rect x="6.3" y="11" width="1.4" height="4" fill="#fff"/><rect x="8.3" y="11" width="1.4" height="4" fill="#fff"/><rect x="1" y="7" width="14" height="1.2" fill="#fff"/><rect x="1" y="5.5" width="1.5" height="4" fill="#fff"/><rect x="13.5" y="5.5" width="1.5" height="4" fill="#fff"/></svg></div>
      <h3>Work out</h3>
      <p>Donec nec justo eget felis facilisis fermentum. Aliquam porttitor mauris sit amet orci. Aenean dignissim pellentesq <span class="more-link">=&gt; more</span></p>
    </div>
  </section>

  <section>
    <h2 class="abs intro-title">Donec nec justo eget felis facilisis fermentum. Aliquam porttitor sit amet orci. Aenean dignissim pellentesque felis</h2>
    <div class="abs rule" style="left:156px;top:447px;width:322px"></div>
    <p class="abs intro-sub">Civamus vestibulum nulla nec ante</p>
    <div class="abs rule" style="left:156px;top:464px;width:322px"></div>
    <div class="col" style="left:156px"><h4>Sed egestas anteet</h4><p>Eros pede semper est, vitae luctus metus libero eu augue. Morbi purus libero, faucibus adipiscing, commodo quis, gravida id, est. Sed lectus. Praesent elementum hendrerit tortor. Ultrices sagittis, mi neque euismod dui, eu pulvinar nunc sapien ornare nisl.</p></div>
    <div class="col" style="left:323px"><h4>Aenean egestas anteet</h4><p>Lorem pede semper est, vitae luctus metus libero eu augue. Morbi purus libero, faucibus adipiscing, commodo quis, gravida id, est. Sed lectus. Praesent elementum hendrerit tortor. Ultrices sagittis, mi neque euismod dui, eu pulvinar nunc sapien ornare nisl.</p></div>
    <a class="pill" style="left:156px;top:550px;width:30px;height:15px">MORE</a>
    <a class="pill" style="left:323px;top:550px;width:30px;height:15px">MORE</a>
    <div class="abs intro-photo" role="img" aria-label="Woman jogging along a tree-lined road"></div>
  </section>

  <section class="abs banner">
    <div class="avatar"><svg width="12" height="12" viewBox="0 0 12 12"><circle cx="6" cy="3.2" r="2.8" fill="var(--navy)"/><path d="M.5 12a5.5 4.5 0 0 1 11 0Z" fill="var(--navy)"/></svg></div>
    <h5 style="left:53px">Donec nec justo eget</h5>
    <p class="quote">" Ede semper est, vitae luctus metus libero eu augue. Morb sipo ipiscing, commodo quis, gravida ..." - <em>Kohn Doe / company name</em></p>
    <h5 style="left:263px">Morbi vitae luctus</h5>
    <div class="field" style="left:263px;top:40px;width:158px;height:17px">enter your email id here ...</div>
    <div class="subscribe">SUBCRIBE</div>
  </section>

  <section>
    <h3 class="lower-title" style="left:156px">Aliquam tincidunt</h3>
    <div class="abs rule" style="left:156px;top:726px;width:155px"></div>
    <div class="post-thumb" style="top:739px;background:#c9a99a" role="img" aria-label="Portrait thumbnail"></div>
    <p class="post-text" style="top:741px">Donec nec justo eget felis facilisis fermentum. Aliquam porttitor<br><b>more &nbsp;=&gt;</b></p>
    <div class="abs rule" style="left:156px;top:780px;width:155px"></div>
    <div class="post-thumb" style="top:794px;background:#5a4a48" role="img" aria-label="Article thumbnail"></div>
    <p class="post-text" style="top:795px">Donec nec justo eget felis facilisis fermentum. Aliquam porttitor<br><b>more &nbsp;=&gt;</b></p>
    <div class="abs rule" style="left:156px;top:835px;width:155px"></div>
    <div class="post-thumb" style="top:848px;background:#8c9a94" role="img" aria-label="Article thumbnail"></div>
    <p class="post-text" style="top:849px">Donec nec justo eget felis facilisis fermentum. Aliquam porttitor<br><b>more &nbsp;=&gt;</b></p>
    <div class="abs rule" style="left:156px;top:889px;width:155px"></div>

    <h3 class="lower-title" style="left:323px">Nunc dignissim risu</h3>
    <div class="abs form-box">
      <p>Sed egestas, ante et vulputate volutpat, eros pede semper est, vitae luctus metus liber</p>
      <div class="field" style="left:13px;top:41px;width:129px;height:17px">name ..</div>
      <div class="field" style="left:13px;top:66px;width:129px;height:17px">email ..</div>
      <div class="field" style="left:13px;top:92px;width:129px;height:34px;border-radius:6px;align-items:flex-start;padding-top:5px">your query ..</div>
      <div class="pill" style="left:13px;top:135px;width:42px;height:17px;font-size:6px;gap:5px">SEND <svg width="7" height="5" viewBox="0 0 7 5"><path d="M0 2.5h6M4 .5l2 2-2 2" stroke="#fff" fill="none" stroke-width="1"/></svg></div>
    </div>

    <h3 class="lower-title" style="left:491px">Aliquam tincidunt</h3>
    <div class="abs rule" style="left:491px;top:726px;width:155px"></div>
    <div class="contact-item" style="top:738px">
      <svg width="11" height="10" viewBox="0 0 11 10"><path d="M5.5 0 11 5H9.5v5H6.5V7h-2v3H1.5V5H0Z" fill="var(--ink)"/></svg>
      <h6>Address</h6><p>some block, steet number, city name,<br>country</p>
    </div>
    <div class="abs rule" style="left:491px;top:776px;width:155px"></div>
    <div class="contact-item" style="top:789px">
      <svg width="10" height="10" viewBox="0 0 10 10"><rect width="10" height="10" rx="2" fill="var(--ink)"/><path d="M3 2.2 4.3 3.6 3.6 4.4a4 4 0 0 0 2 2l.8-.7 1.4 1.3-.9 1A5.5 5.5 0 0 1 2 3.1Z" fill="#fff"/></svg>
      <h6>Phone</h6><p>(000) 777 777 7777<br>(000) 888 888 8888</p>
    </div>
    <div class="abs rule" style="left:491px;top:827px;width:155px"></div>
    <div class="contact-item" style="top:840px">
      <svg width="11" height="8" viewBox="0 0 11 8"><rect width="11" height="8" fill="var(--ink)"/><path d="M0 0l5.5 4.5L11 0" stroke="#fff" fill="none" stroke-width=".8"/></svg>
      <h6>Email us</h6><p>info@sitename.com<br>sales@sitename.com<br>company@sitename.com</p>
    </div>
    <div class="abs rule" style="left:491px;top:889px;width:155px"></div>
  </section>

  <footer class="abs footer">
    <span class="social" style="left:583px" aria-label="Social link"></span>
    <span class="social" style="left:605px" aria-label="Social link"></span>
    <span class="social" style="left:627px" aria-label="Social link"></span>
  </footer>
</div>
</body>
</html>
```